Leadership and Team Coaching Blog Template for my company, Fenwick Marlow Pty Ltd

I need a consistent design I can use for publications. I am a leadership coach as well as a team coach and I also am a pretty good facilitator. I am to help people be their best both as individuals and as teams so as I enter semi-retirement I've been writing short articles to support my business. The final design should be flexible and elegant so you can tell the difference between different articles. It should also communicate confidence, energy and expertise and invite you to read further. I love blue and have attached my current logo. Not wedded to using it but clients recognise it and am sure someone clever can do something interesting with it

Target Market(s)

middle and senior leaders and Board members

Industry/Entity Type

It Company

Font styles to use
Sans Serif

Colors
0392cd
3176b5
3276b5
886aae
33b8a4
00a990
a54499
c588bc
876aae

Requirements
Must have
• flexibility to be able to re-use for different publications
Nice to have
• eye catching images
• elegant line drawing
Should not have
• clip art

```html
<!DOCTYPE html>
<html lang="en">
<head>
<meta charset="utf-8">
<title>Fenwick Marlow Pty Ltd — Blog</title>
<link rel="stylesheet" href="https://fonts.googleapis.com/css2?family=Cinzel:wght@400;500&family=Montserrat:wght@400;500;600&family=Open+Sans:wght@400;600&display=swap">
<style>
  :root {
    --blue: #3176b5;
    --blue-bright: #0392cd;
    --purple: #886aae;
    --purple-deep: #6f4f9c;
    --teal: #33b8a4;
    --teal-deep: #00a990;
    --footer: #9b3f92;
    --ink: #333333;
    --body-text: #555555;
    --icon: #8f8f8f;
    --rule: #e3e3e3;
    --sun-1: #f7a21b;
    --sun-2: #e4641a;
    --sun-3: #7a2a14;
  }
  * { box-sizing: border-box; margin: 0; padding: 0; }
  html, body { width: 1200px; height: 2446px; overflow: hidden; }
  body {
    position: relative;
    font-family: "Open Sans", sans-serif;
    color: var(--body-text);
    background: radial-gradient(circle at 50% 5%, #ffffff 0%, #f4f4f4 45%, #ececec 100%);
  }
  a { color: inherit; text-decoration: none; }

  /* Header */
  .brand {
    position: absolute; top: 58px; left: 0; width: 1200px;
    text-align: center; font-family: "Montserrat", sans-serif; font-weight: 500;
    color: var(--blue); font-size: 26px; line-height: 30px; letter-spacing: 3px;
    text-transform: uppercase;
  }
  .main-nav {
    position: absolute; top: 137px; left: 130px; width: 938px; height: 52px;
    background: linear-gradient(#4d8bcb, var(--blue));
    display: flex; font-family: "Montserrat", sans-serif; font-size: 15px; font-weight: 500;
    color: #fff; text-transform: uppercase;
  }
  .main-nav a { flex: 1; display: flex; align-items: center; justify-content: center; }
  .main-nav a.is-active { background: linear-gradient(#a57cc0, var(--purple)); flex: 0 0 148px; }

  /* Hero */
  .hero {
    position: absolute; top: 189px; left: 130px; width: 938px; height: 388px; overflow: hidden;
    background: radial-gradient(ellipse at 72% 78%, #ffe27a 0%, var(--sun-1) 18%, var(--sun-2) 48%, var(--sun-3) 100%);
  }
  .hero-title {
    position: absolute; top: 128px; left: 208px; width: 524px; text-align: center;
    font-family: "Cinzel", serif; font-weight: 400; color: #fff; text-transform: uppercase;
    border-top: 1px solid rgba(255,255,255,.7); border-bottom: 1px solid rgba(255,255,255,.7);
    padding: 8px 0 10px;
  }
  .hero-title .line-1 { display: block; font-size: 38px; line-height: 44px; letter-spacing: 1px; }
  .hero-title .line-2 { display: block; font-size: 30px; line-height: 36px; }
  .hero-arrow {
    position: absolute; top: 170px; width: 28px; height: 42px; background: #fff;
    display: flex; align-items: center; justify-content: center;
  }
  .hero-arrow.prev { left: 0; }
  .hero-arrow.next { right: 0; }

  /* Feature cards */
  .feature-card { position: absolute; top: 606px; width: 298px; }
  .feature-card .photo { height: 173px; }
  .feature-card .tag {
    margin-top: 20px; font-family: "Montserrat", sans-serif; font-size: 12px; font-weight: 500;
    color: var(--purple); text-transform: uppercase;
  }
  .feature-card h3 { margin-top: 10px; font-family: "Montserrat", sans-serif; font-weight: 400; font-size: 17px; color: var(--ink); }
  .excerpt { margin-top: 8px; font-size: 12px; line-height: 20px; color: var(--body-text); }
  .read-more {
    display: inline-block; margin-top: 8px; font-family: "Montserrat", sans-serif; font-size: 13px;
    color: var(--blue-bright); text-transform: uppercase;
  }
  .section-rule { position: absolute; top: 998px; left: 130px; width: 615px; border: 0; border-top: 1px solid var(--rule); }

  /* Post list */
  .post { position: absolute; left: 130px; width: 615px; height: 212px; }
  .post .photo { position: absolute; left: 0; top: 0; width: 299px; height: 212px; }
  .post .body { position: absolute; left: 322px; top: 0; width: 293px; }
  .post h2 { font-family: "Montserrat", sans-serif; font-weight: 500; font-size: 16px; line-height: 24px; color: var(--blue); }
  .post .excerpt { margin-top: 8px; }
  .share { position: absolute; right: 0; bottom: 0; display: flex; gap: 6px; }
  .share span {
    width: 24px; height: 24px; border-radius: 50%; border: 1px solid #dcdcdc; background: #fff;
    display: flex; align-items: center; justify-content: center;
  }
  .share svg { width: 11px; height: 11px; fill: none; stroke: var(--icon); stroke-width: 1.6; stroke-linecap: round; stroke-linejoin: round; }

  /* Sidebar */
  .about-panel { position: absolute; top: 606px; left: 771px; width: 297px; height: 418px; background: var(--purple); overflow: hidden; }
  .about-panel .photo { height: 200px; }
  .about-panel .curve { position: absolute; top: 178px; left: 0; }
  .about-panel .content { position: absolute; top: 196px; left: 22px; right: 22px; text-align: center; color: #fff; }
  .about-panel h3 { font-family: "Montserrat", sans-serif; font-weight: 400; font-size: 20px; }
  .about-panel p { margin-top: 12px; font-size: 12px; line-height: 20px; }
  .outline-btn {
    display: inline-block; margin-top: 18px; padding: 8px 20px; border: 2px solid #fff;
    font-family: "Montserrat", sans-serif; font-size: 13px; text-transform: uppercase;
  }

  .widget { position: absolute; left: 771px; width: 297px; background: #fff; border: 1px solid var(--rule); }
  .widget-head {
    height: 49px; padding-left: 27px; display: flex; align-items: center; color: #fff;
    font-family: "Montserrat", sans-serif; font-size: 20px; text-transform: uppercase;
  }
  .popular { top: 1043px; height: 612px; }
  .popular .widget-head { background: linear-gradient(var(--teal), var(--teal-deep)); }
  .popular-item { margin: 17px 18px 0; text-align: center; }
  .popular-item .photo { height: 124px; }
  .popular-item h4 { margin-top: 16px; font-family: "Montserrat", sans-serif; font-weight: 400; font-size: 16px; color: var(--purple); }
  .popular-item p { margin-top: 6px; font-size: 12px; line-height: 20px; color: var(--body-text); padding: 0 12px; }
  .popular-item .read-more { color: var(--teal-deep); margin-top: 6px; }

  .archives { top: 1681px; height: 376px; }
  .archives .widget-head { background: linear-gradient(#9278b8, var(--purple-deep)); }
  .archives ul { list-style: none; padding: 14px 0 0 34px; }
  .archives li { display: flex; align-items: center; gap: 10px; height: 34px; font-size: 12px; color: var(--body-text); }

  /* Footer */
  .site-footer { position: absolute; top: 2155px; left: 0; width: 1200px; height: 291px; background: var(--footer); color: #fff; }
  .footer-col { position: absolute; top: 53px; }
  .footer-col h5 { font-family: "Montserrat", sans-serif; font-weight: 500; font-size: 15px; text-transform: uppercase; }
  .footer-links { list-style: none; margin-top: 14px; font-size: 13px; }
  .footer-links li { height: 30px; }
  .social { display: flex; gap: 10px; margin-top: 14px; }
  .social span {
    width: 36px; height: 36px; border-radius: 50%; background: #fff;
    display: flex; align-items: center; justify-content: center;
  }
  .social svg { width: 16px; height: 16px; fill: none; stroke: var(--footer); stroke-width: 1.8; stroke-linecap: round; stroke-linejoin: round; }
  .newsletter p { margin-top: 10px; font-size: 13px; }
  .subscribe { display: flex; margin-top: 10px; height: 36px; }
  .subscribe .field { width: 206px; background: #fff; color: #aaa; font-size: 11px; display: flex; align-items: center; padding-left: 12px; text-transform: uppercase; }
  .subscribe .btn { width: 100px; background: var(--blue-bright); font-family: "Montserrat", sans-serif; font-weight: 600; font-size: 13px; display: flex; align-items: center; justify-content: center; text-transform: uppercase; }
  .footer-rule { position: absolute; top: 233px; left: 140px; width: 920px; border-top: 1px solid rgba(255,255,255,.3); }
  .copyright { position: absolute; top: 250px; left: 140px; font-size: 11px; color: rgba(255,255,255,.8); }

  /* Photo placeholders */
  .tone-office { background: linear-gradient(135deg, #c9c2b8, #7d7468 60%, #4c4641); }
  .tone-meeting { background: linear-gradient(135deg, #e4e6ea, #9aa8b8 55%, #55667a); }
  .tone-light { background: linear-gradient(135deg, #e9ecef, #b9c3cc 60%, #7d8b97); }
  .tone-bulb { background: radial-gradient(circle at 50% 40%, #ffe7a1, #d99738 30%, #5a3417 70%, #2c1a0e); }
  .tone-desk { background: linear-gradient(135deg, #b9a48c, #7a6656 60%, #3f332c); }
  .tone-sketch { background: linear-gradient(135deg, #a08366, #d7cbbb 55%, #8c7862); }
  .tone-sky { background: linear-gradient(#c8d4df, #eef1f4); }
  .tone-team { background: linear-gradient(135deg, #dfe6ee, #9fb2c6 55%, #5f738a); }
</style>
</head>
<body>

<svg width="0" height="0" style="position:absolute" aria-hidden="true">
  <defs>
    <symbol id="i-share" viewBox="0 0 16 16"><circle cx="4" cy="8" r="2"/><circle cx="12" cy="3.5" r="2"/><circle cx="12" cy="12.5" r="2"/><path d="M5.8 7 10.2 4.5M5.8 9 10.2 11.5"/></symbol>
    <symbol id="i-mail" viewBox="0 0 16 16"><rect x="1.5" y="3.5" width="13" height="9" rx="1"/><path d="M1.5 4.5 8 9l6.5-4.5"/></symbol>
    <symbol id="i-link" viewBox="0 0 16 16"><path d="M6.5 9.5 9.5 6.5M7 4.5l1.5-1.5a2.8 2.8 0 0 1 4 4L11 8.5M9 11.5 7.5 13a2.8 2.8 0 0 1-4-4L5 7.5"/></symbol>
    <symbol id="i-heart" viewBox="0 0 16 16"><path d="M8 13.5S2 10 2 6a3 3 0 0 1 6-1 3 3 0 0 1 6 1c0 4-6 7.5-6 7.5z"/></symbol>
    <symbol id="i-bookmark" viewBox="0 0 16 16"><path d="M4 2h8v12l-4-3-4 3z"/></symbol>
    <symbol id="i-chat" viewBox="0 0 16 16"><path d="M2 3h12v8H7l-3 3v-3H2z"/></symbol>
  </defs>
</svg>

<header>
  <div class="brand">Fenwick Marlow</div>
  <nav class="main-nav">
    <a class="is-active" href="#">Home</a>
    <a href="#">About Us</a>
    <a href="#">Our Articles</a>
    <a href="#">Blogs</a>
    <a href="#">Resources</a>
    <a href="#">Contact</a>
  </nav>
</header>

<section class="hero" role="img" aria-label="Two climbers silhouetted on a rock, one helping the other up, against an orange sunset">
  <h1 class="hero-title"><span class="line-1">We are a leadership</span><span class="line-2">&amp; Team Coaching</span></h1>
  <a class="hero-arrow prev" href="#" aria-label="Previous slide"><svg width="8" height="12" viewBox="0 0 8 12"><path d="M6 1L1 6l5 5" fill="none" stroke="#333" stroke-width="1.6"/></svg></a>
  <a class="hero-arrow next" href="#" aria-label="Next slide"><svg width="8" height="12" viewBox="0 0 8 12"><path d="M2 1l5 5-5 5" fill="none" stroke="#333" stroke-width="1.6"/></svg></a>
</section>

<main>
  <article class="feature-card" style="left:130px">
    <div class="photo tone-office" role="img" aria-label="Team standing around a table in an open office workshop"></div>
    <div class="tag">Lateset</div>
    <h3>Morbi ornare elit Integer</h3>
    <p class="excerpt">congue augue et malesuada iaculis ipsum dui aliquet felis at cursus magna nisl nec elit Praesent elementum elit at tellus nec ultricies sit amet porttitor mattis enim In massa libero interdum</p>
    <a class="read-more" href="#">Read more</a>
  </article>
  <article class="feature-card" style="left:452px">
    <div class="photo tone-meeting" role="img" aria-label="Man in a blue shirt addressing colleagues around a boardroom table"></div>
    <div class="tag">Featured</div>
    <h3>Morbi ornare elit Integer</h3>
    <p class="excerpt">congue augue et malesuada iaculis ipsum dui aliquet felis at cursus magna nisl nec elit Praesent elementum elit at tellus nec ultricies sit amet porttitor mattis enim In massa libero interdum</p>
    <a class="read-more" href="#">Read more</a>
  </article>

  <hr class="section-rule">

  <article class="post" style="top:1032px">
    <div class="photo tone-light" role="img" aria-label="Business team meeting around a white table in a bright room"></div>
    <div class="body">
      <h2>Cum sociis natoque penatibus et magnis dis parturient</h2>
      <p class="excerpt">congue augue et malesuada iaculis ipsum dui aliquet felis at cursus magna nisl nec elit Praesent elementum elit at tellus nec ultricies sit amet t ac nisl Cum sociis natoque penatibus et magnis dis parturient montes nascetur ridiculus mus In iaculis facilisis massa Etiam eu urna Seddum</p>
      <a class="read-more" href="#">Read more</a>
    </div>
    <div class="share" aria-label="Share"><span><svg><use href="#i-share"/></svg></span><span><svg><use href="#i-mail"/></svg></span><span><svg><use href="#i-link"/></svg></span><span><svg><use href="#i-heart"/></svg></span><span><svg><use href="#i-bookmark"/></svg></span></div>
  </article>

  <article class="post" style="top:1304px">
    <div class="photo tone-meeting" role="img" aria-label="Presenter speaking to a seated group in a glass-walled meeting room"></div>
    <div class="body">
      <h2>Nullam enim leo egestas id condiment laoreet</h2>
      <p class="excerpt">congue augue et malesuada iaculis ipsum dui aliquet felis at cursus magna nisl nec elit Praesent elementum elit at tellus nec ultricies sit amet t ac nisl Cum sociis natoque penatibus et magnis dis parturient montes nascetur ridiculus mus In iaculis facilisis massa Etiam eu urna Seddum</p>
      <a class="read-more" href="#">Read more</a>
    </div>
    <div class="share" aria-label="Share"><span><svg><use href="#i-share"/></svg></span><span><svg><use href="#i-mail"/></svg></span><span><svg><use href="#i-link"/></svg></span><span><svg><use href="#i-heart"/></svg></span><span><svg><use href="#i-bookmark"/></svg></span></div>
  </article>

  <article class="post" style="top:1575px">
    <div class="photo tone-bulb" role="img" aria-label="Person standing before a glowing light-bulb shaped doorway"></div>
    <div class="body">
      <h2>Nullam enim leo egestas id condiment laoreet</h2>
      <p class="excerpt">congue augue et malesuada iaculis ipsum dui aliquet felis at cursus magna nisl nec elit Praesent elementum elit at tellus nec ultricies sit amet t ac nisl Cum sociis natoque penatibus et magnis dis parturient montes nascetur ridiculus mus In iaculis facilisis massa Etiam eu urna Seddum</p>
      <a class="read-more" href="#">Read more</a>
    </div>
    <div class="share" aria-label="Share"><span><svg><use href="#i-share"/></svg></span><span><svg><use href="#i-mail"/></svg></span><span><svg><use href="#i-link"/></svg></span><span><svg><use href="#i-heart"/></svg></span><span><svg><use href="#i-bookmark"/></svg></span></div>
  </article>

  <article class="post" style="top:1842px">
    <div class="photo tone-desk" role="img" aria-label="Colleagues gathered around a desk covered with notes and papers"></div>
    <div class="body">
      <h2>Nullam enim leo egestas id condiment laoreet</h2>
      <p class="excerpt">congue augue et malesuada iaculis ipsum dui aliquet felis at cursus magna nisl nec elit Praesent elementum elit at tellus nec ultricies sit amet t ac nisl Cum sociis natoque penatibus et magnis dis parturient montes nascetur ridiculus mus In iaculis facilisis massa Etiam eu urna Seddum</p>
      <a class="read-more" href="#">Read more</a>
    </div>
    <div class="share" aria-label="Share"><span><svg><use href="#i-share"/></svg></span><span><svg><use href="#i-mail"/></svg></span><span><svg><use href="#i-link"/></svg></span><span><svg><use href="#i-heart"/></svg></span><span><svg><use href="#i-bookmark"/></svg></span></div>
  </article>
</main>

<aside>
  <section class="about-panel">
    <div class="photo tone-sketch" role="img" aria-label="Hand sketching a leadership mind map on paper at a wooden desk"></div>
    <svg class="curve" width="297" height="40" viewBox="0 0 297 40" aria-hidden="true"><path d="M0 22 Q148 -4 297 22 V40 H0 Z" fill="#886aae"/></svg>
    <div class="content">
      <h3>LITTLE ABOUT US</h3>
      <p>Aommodo a mi Morbi ornare gravida elit Integer congue augue et malesuada iaculis ipsum dui aliquet felis at cursus magna nisl nec elit Praesent elementum elit at tellus nec ultricies sit amet porttitor mattis</p>
      <a class="outline-btn" href="#">Read more</a>
    </div>
  </section>

  <section class="widget popular">
    <div class="widget-head">Popular Posts</div>
    <div class="popular-item">
      <div class="photo tone-sky" role="img" aria-label="Flock of birds flying in formation across a pale sky"></div>
      <h4>Aommodo Morbi ornare</h4>
      <p>gravida elit Integer congue augue et malesuada iaculis ipsum dui aliquet felis at cursus magna nisl nec elit Praesent</p>
      <a class="read-more" href="#">Read more</a>
    </div>
    <div class="popular-item">
      <div class="photo tone-team" role="img" aria-label="Colleagues reviewing ideas together on a glass board"></div>
      <h4>Donec dictum lectus non</h4>
      <p>gravida elit Integer congue augue et malesuada iaculis ipsum dui aliquet felis at cursus magna nisl nec elit Praesent</p>
      <a class="read-more" href="#">Read more</a>
    </div>
  </section>

  <section class="widget archives">
    <div class="widget-head">Archives</div>
    <ul>
      <li><svg width="6" height="9" viewBox="0 0 6 9"><path d="M0 0l6 4.5L0 9z" fill="#999"/></svg>June 2015 (3)</li>
      <li><svg width="6" height="9" viewBox="0 0 6 9"><path d="M0 0l6 4.5L0 9z" fill="#999"/></svg>June 2015 (3)</li>
      <li><svg width="6" height="9" viewBox="0 0 6 9"><path d="M0 0l6 4.5L0 9z" fill="#999"/></svg>May 2015 (3)</li>
      <li><svg width="6" height="9" viewBox="0 0 6 9"><path d="M0 0l6 4.5L0 9z" fill="#999"/></svg>April 2015 (2)</li>
      <li><svg width="6" height="9" viewBox="0 0 6 9"><path d="M0 0l6 4.5L0 9z" fill="#999"/></svg>March 2015 (5)</li>
      <li><svg width="6" height="9" viewBox="0 0 6 9"><path d="M0 0l6 4.5L0 9z" fill="#999"/></svg>February 2015 (2)</li>
      <li><svg width="6" height="9" viewBox="0 0 6 9"><path d="M0 0l6 4.5L0 9z" fill="#999"/></svg>January 2015 (1)</li>
      <li><svg width="6" height="9" viewBox="0 0 6 9"><path d="M0 0l6 4.5L0 9z" fill="#999"/></svg>December 2014 (3)</li>
    </ul>
  </section>
</aside>

<footer class="site-footer">
  <div class="footer-col" style="left:147px">
    <h5>Usefull Links</h5>
    <ul class="footer-links"><li>Home</li><li>About Us</li><li>Our Articles</li><li>News</li></ul>
  </div>
  <div class="footer-col" style="left:310px;top:78px">
    <ul class="footer-links"><li>Latest Blogs</li><li>Archive</li><li>Resources</li><li>Contact</li></ul>
  </div>
  <div class="footer-col" style="left:483px">
    <h5>Follow Us</h5>
    <div class="social" aria-label="Follow links"><span><svg><use href="#i-share"/></svg></span><span><svg><use href="#i-chat"/></svg></span><span><svg><use href="#i-mail"/></svg></span><span><svg><use href="#i-link"/></svg></span></div>
  </div>
  <div class="footer-col newsletter" style="left:730px">
    <h5>Sign up for newsletters</h5>
    <p>Please sign up here for latest news</p>
    <div class="subscribe"><div class="field">Email address</div><div class="btn">Subscribe</div></div>
  </div>
  <div class="footer-rule"></div>
  <div class="copyright">© 2016 Company Name&nbsp; All right reserved&nbsp; Term of Use</div>
</footer>

</body>
</html>
```